Stationary Design for Quince consultant and support company

We need new stationary designed for a London based support company that provide on-site and remote support services for Quince products. Our clients are both consumers and businesses.

We would like a letterhead, compliment slip, business card and possibly an e-mail signature designed.

Business card designs can be either 1 side or 2, depending on designs we receive we may choose a preference for 1 or 2 sides later on in the design stage.

Designs needs to be at least 300dpi and should be done using CMYK colours.

We want the design to be bold, easy to read, clean and professional.

We have attached our company logo in 2 colour variations (if you need any other source files then please ask).

Our logo colours are as follows:

Blue (85, 50, 0, 0) and Green (50, 0, 100, 0)

We use two different suppliers for out stationary so here are the size dimensions for both. Unfortunately they are ever so slightly different size wise so hopefully we can get something that accommodates both, we can provide dimensions if required for final versions.

Some fonts that have been used before with our company are Probert (for tagline on our company logo) and previously had Nauman used, however we are very much open to seeing what the designers come up with and the fonts mentioned are not a requirement.
Updates

Company details for designs (however the template should be editable for multiple staff) Vorn-Q Ltd. Registered Office: 62-74 Marrow Lane London N7 3QT 020 7195 8843 www.vorn-q.co info@vorn-q.co Company is Registered in England and Wales Company No. 06412853 Directors details (if you want to make the template using his details), rest of the details are as above Dan Myles Director dan@vorn-q.co

Hi all, Thank you for your submissions so far. Could we please ask that you don't use the logo with the tagline from our website for the stationary designs and only the logos provided in the design brief. For the business cards we are looking at normal rectangular business cards to be used and we can provide a template guide for size if needed, please just ask. Regards Vorn-Q Team

Target Market(s)

Our target market are consumers (of all ages) and small/medium businesses.

Industry/Entity Type

Business

Font styles to use
Serif
Sans Serif

Requirements
Must have
• At least business card, letterhead and compliment slip submitted (we need all 3 designed this time round)
Should not have
• Business cards should not have the writing "registered office" (letterheads and compliment slips can along the bottom edge)

```html
<!DOCTYPE html>
<html lang="en">
<head>
<meta charset="utf-8">
<title>Vorn-Q Business Card</title>
<link rel="stylesheet" href="https://fonts.googleapis.com/css2?family=Open+Sans:wght@400;600;700;800&display=swap">
<style>
  :root {
    --blue: #1a73c4;
    --blue-dark: #0f5fa8;
    --green: #7cc242;
    --ink: #1b1b1b;
    --grey-text: #555c63;
    --paper: #ffffff;
    --backdrop: #e9e6e1;
  }
  * { box-sizing: border-box; margin: 0; padding: 0; }
  html, body {
    width: 1200px; height: 1024px; overflow: hidden;
    background: var(--backdrop);
    font-family: "Open Sans", Arial, sans-serif;
  }
  .sheet { position: relative; width: 1200px; height: 1024px; }

  .card {
    position: absolute; left: 250px;
    width: 700px; height: 400px;
    box-shadow: 0 6px 18px rgba(0,0,0,0.18);
    overflow: hidden;
  }
  .card--front { top: 82px; background: var(--paper); }
  .card--back { top: 542px; background: linear-gradient(160deg, #1f7dcc 0%, var(--blue-dark) 100%); }

  /* front */
  .brand-name {
    position: absolute; font-weight: 800; letter-spacing: 2px;
    text-transform: uppercase;
  }
  .card--front .brand-name {
    left: 60px; top: 148px; font-size: 58px; color: var(--ink);
  }
  .divider {
    position: absolute; left: 372px; top: 40px; width: 1px; height: 280px;
    background: linear-gradient(to bottom, rgba(0,0,0,0), #d5d8db 30%, #d5d8db 70%, rgba(0,0,0,0));
  }
  .contact { position: absolute; left: 400px; top: 44px; color: var(--grey-text); font-size: 15px; line-height: 1.55; }
  .contact__name { color: var(--blue); font-weight: 700; font-size: 22px; letter-spacing: 1px; text-transform: uppercase; line-height: 1.2; }
  .contact__role { color: var(--green); font-size: 17px; margin-bottom: 4px; }
  .contact__address { margin-top: 30px; margin-bottom: 8px; }
  .contact__line { display: flex; align-items: center; gap: 8px; }
  .contact__line svg { width: 14px; height: 14px; flex: none; }

  .band { position: absolute; left: 0; bottom: 0; width: 700px; height: 44px; }
  .company-no {
    position: absolute; right: 22px; bottom: 12px;
    color: #fff; font-size: 14px; letter-spacing: 0.5px;
  }

  /* back */
  .card--back .brand-name {
    left: 0; width: 100%; top: 150px; text-align: center;
    font-size: 78px; color: #fff; letter-spacing: 4px;
  }
  .back-url {
    position: absolute; left: 36px; bottom: 36px;
    color: #fff; font-size: 15px; letter-spacing: 3px;
  }
</style>
</head>
<body>
<main class="sheet">

  <section class="card card--front" aria-label="Business card front">
    <div class="brand-name">Vorn-Q</div>
    <div class="divider"></div>

    <div class="contact">
      <div class="contact__name">Dan Myles</div>
      <div class="contact__role">Director</div>
      <div class="contact__line">
        <svg viewBox="0 0 14 14"><rect x="0.5" y="2.5" width="13" height="9" fill="var(--blue)"/><path d="M1 3l6 5 6-5" stroke="#fff" stroke-width="1.2" fill="none"/></svg>
        dan@vorn-q.co
      </div>

      <div class="contact__address">
        62-74 Marrow Lane London<br>
        N7 3QT&nbsp;&nbsp;020 7195 8843
      </div>
      <div class="contact__line">
        <svg viewBox="0 0 14 14"><path d="M3 1h3l1 3-2 1.5c.8 1.7 2 2.9 3.5 3.5L10 7l3 1v3c0 1-1 2-2 2C5.5 13 1 8.5 1 3c0-1 1-2 2-2z" fill="var(--blue)"/></svg>
        062-074-3195
      </div>
      <div class="contact__line">
        <svg viewBox="0 0 14 14"><rect x="0.5" y="2.5" width="13" height="9" fill="var(--blue)"/><path d="M1 3l6 5 6-5" stroke="#fff" stroke-width="1.2" fill="none"/></svg>
        info@vorn-q.co
      </div>
      <div class="contact__line">
        <svg viewBox="0 0 14 14"><circle cx="7" cy="7" r="6.3" fill="var(--blue)"/><path d="M1 7h12M7 1c-2.5 3-2.5 9 0 12M7 1c2.5 3 2.5 9 0 12" stroke="#fff" stroke-width="0.9" fill="none"/></svg>
        www.vorn-q.co
      </div>
    </div>

    <svg class="band" viewBox="0 0 700 44" preserveAspectRatio="none" aria-hidden="true">
      <rect x="0" y="0" width="700" height="44" fill="var(--blue)"/>
      <polygon points="440,0 700,0 700,44 460,44 448,22" fill="var(--green)"/>
    </svg>
    <div class="company-no">Company No. 06412853</div>
  </section>

  <section class="card card--back" aria-label="Business card back">
    <div class="brand-name">Vorn-Q</div>
    <div class="back-url">www.vorn-q.co</div>
  </section>

</main>
</body>
</html>
```